Melissa Dorvan Personal Business Card

I like orange. It's would better if my card have an orange background
Address: 5820 Halvers Lane #417
San Jose
California
US
Tel: 4085172049

Industry/Entity Type

Business

```html
<!DOCTYPE html>
<html lang="en">
<head>
<meta charset="utf-8">
<title>Melissa Dorvan – Business Card</title>
<link href="https://fonts.googleapis.com/css2?family=Merienda:wght@700&family=Tinos&display=swap" rel="stylesheet">
<style>
  :root {
    --page-bg: #ffffff;
    --card-orange: #e57818;
    --name-white: #ffffff;
    --ink-dark: #2a2624;
    --wedge-light: #ffffff;
    --wedge-mid: #c9ccce;
    --wedge-dark: #3f4346;
  }
  html, body {
    margin: 0;
    padding: 0;
    width: 1200px;
    height: 1000px;
    overflow: hidden;
    background: var(--page-bg);
  }
  .business-card {
    position: absolute;
    left: 237px;
    top: 258px;
    width: 755px;
    height: 457px;
    background: var(--card-orange);
    overflow: hidden;
  }
  .corner-wedge {
    position: absolute;
    left: 0;
    top: 0;
    width: 755px;
    height: 457px;
  }
  .holder-name {
    position: absolute;
    left: 68px;
    top: 62px;
    margin: 0;
    font-family: "Merienda", cursive;
    font-weight: 700;
    font-size: 31px;
    color: var(--name-white);
    letter-spacing: -0.3px;
  }
  .contact-line {
    position: absolute;
    left: 70px;
    display: flex;
    align-items: flex-start;
    font-family: "Tinos", "Times New Roman", serif;
    font-size: 25px;
    line-height: 30px;
    color: var(--ink-dark);
  }
  .contact-line svg {
    width: 22px;
    height: 24px;
    margin-top: 2px;
    margin-right: 5px;
    flex: none;
  }
  .contact-address { top: 155px; }
  .contact-phone { top: 239px; }
</style>
</head>
<body>
  <div class="business-card">
    <svg class="corner-wedge" viewBox="0 0 755 457" role="img" aria-label="Fanned grey stripes sweeping from the bottom-left corner">
      <defs>
        <linearGradient id="wedgeShade" x1="0" y1="185" x2="0" y2="457" gradientUnits="userSpaceOnUse">
          <stop offset="0" stop-color="var(--wedge-light)"/>
          <stop offset="0.55" stop-color="var(--wedge-mid)"/>
          <stop offset="1" stop-color="var(--wedge-dark)"/>
        </linearGradient>
      </defs>
      <polygon points="0,457 755,185 755,457" fill="url(#wedgeShade)"/>
    </svg>

    <h1 class="holder-name">Melissa Dorvan</h1>

    <div class="contact-line contact-address">
      <svg viewBox="0 0 22 24" aria-hidden="true">
        <polygon points="11,3 1,10 21,10" fill="#fff" stroke="#222" stroke-width="1.2"/>
        <rect x="2" y="11" width="18" height="11" fill="#fff" stroke="#222" stroke-width="1.2"/>
        <rect x="5" y="15" width="6" height="3" fill="#222"/>
      </svg>
      <span>5820 Halvers Lane #417<br>San Jose California US</span>
    </div>

    <div class="contact-line contact-phone">
      <svg viewBox="0 0 22 24" aria-hidden="true">
        <path d="M15 3 C8 4 4 10 5 17 C5.5 20 7 22 8 22 L11 19 L9 15 C9 11 11 8 14 7 L17 5 Z" fill="#fff" stroke="#222" stroke-width="1.2" stroke-linejoin="round"/>
      </svg>
      <span>4085172049</span>
    </div>
  </div>
</body>
</html>
```